812 EDDM FLYER FOR CARPET CLEANING & WINDOW WASHING

Full Size Double Sided full color EDDM mailer

****PLEASE MAKE FONT TYPE, SIZE, COLOR, SPACING SAME AS IS EXAMPLE FLYER*******

***I have uploaded LOGO... It is on the VAN WRAP 812 CLEANING & RESTORATION

I have included an EDDM flyer and want my flyer to look like the example I uploaded.

I wanted to make it look Better & add my images and content. I have included the content under Must Haves......

Raindrop background

****Not all images will be used. Each service requires 2 images as seen on examply flyer... Please pic best 2 for each service, I can purchase new stock photo if needed

Target Market(s)

Residential Home Owners

Industry/Entity Type

Cleaning Service

Font styles to use
Serif

Colors
0555a3
ec1f27
fbed22
ffc214

Requirements
Must have
• Look Like Example EDDM postcard uploaded
• My images & content
• CARPET CLEANING Safe Eco-Friendly Truck Mounted Steam Cleaning. Say goodbye to those ugly carpet stains.
• WINDOW WASHING Interior/Exterior & Screens. Crystal Clear & Streak Free Windows
• POWER WASHING: Soft Wash & Power Wash. Safely cleans
• WATER DAMAGE: Got Mold or Water damage? Free IR Imaging Detection
• TILE & GROUT: Clean, Restore & Rejuvenate Tile, Grout & Stone
• MAINTENANCE: Professional & dependable repairs. We can Fit It!
• Call Today! 858-555-0147
• www.TidyNorth812.example
• ECO FRIENDLY CLEANING
• San Diego’s Trusted Cleaning Specialists

```html
<!DOCTYPE html>
<html lang="en">
<head>
<meta charset="utf-8">
<title>812 Cleaning &amp; Restoration – EDDM Mailer</title>
<link rel="stylesheet" href="https://fonts.googleapis.com/css2?family=Poppins:wght@600;700&family=Lato:wght@400;700&family=Arimo:wght@400;700&display=swap">
<style>
  :root{
    --stage:#595959;
    --sky:#1f7dc8;
    --navy:#143f8a;
    --navy-deep:#0e2f6e;
    --pill:#0b3f8f;
    --gold:#f7b500;
    --gold-text:#ffc214;
    --white:#ffffff;
    --ink:#1b1b1b;
    --brand-blue:#0555a3;
  }
  *{box-sizing:border-box;margin:0;padding:0}
  html,body{width:1200px;height:1200px;overflow:hidden}
  body{background:var(--stage);position:relative;font-family:"Lato",sans-serif}
  .card{position:absolute;overflow:hidden;box-shadow:3px 4px 8px rgba(0,0,0,.45)}
  .abs{position:absolute}
  .photo{position:absolute}

  /* FRONT */
  .front{left:74px;top:99px;width:715px;height:477px;background:var(--sky)}
  .logo-box{left:26px;top:14px;width:331px;height:80px;background:var(--white);display:flex;align-items:center;gap:12px;padding-left:18px}
  .logo-dot{width:42px;height:42px;border-radius:50%;background:var(--gold)}
  .logo-name{font-family:"Poppins",sans-serif;font-weight:700;color:var(--brand-blue);font-size:22px;line-height:1}
  .front .title{right:26px;top:12px;text-align:right;font-family:"Poppins",sans-serif;font-weight:700;color:var(--white);font-size:37px;line-height:46px}
  .front .slogan{right:26px;top:103px;font-family:"Poppins",sans-serif;font-weight:600;color:var(--gold-text);font-size:25px}
  .call-pill{left:363px;top:139px;width:331px;height:35px;border-radius:18px;background:var(--pill);color:var(--white);font-family:"Poppins",sans-serif;font-weight:600;font-size:24px;line-height:35px;text-align:center;white-space:nowrap}
  .frame{border:2px solid var(--white)}
  .band{left:0;width:100%;background:radial-gradient(circle at 30% 40%,#1d4f9e 0%,var(--navy) 55%,var(--navy-deep) 100%)}
  .front .band{top:294px;height:145px}
  .services{left:26px;top:302px;width:680px;display:grid;grid-template-columns:339px 339px;grid-auto-flow:column;grid-template-rows:repeat(3,46px)}
  .service{display:flex;gap:6px}
  .service .num,.service h3{color:var(--gold-text);font-size:14px;font-weight:400;line-height:15px}
  .service p{color:var(--white);font-size:10.5px;line-height:13px}
  .service .tag{color:var(--gold-text)}
  .url-bar{left:0;width:100%;height:38px;background:var(--gold);color:var(--ink);font-size:14px;letter-spacing:3px;text-align:center;line-height:38px}
  .front .url-bar{top:439px}

  /* BACK */
  .back{left:413px;top:645px;width:717px;height:478px;background:var(--white)}
  .back .band{top:264px;height:175px;width:358px;border-top:2px solid var(--sky)}
  .eco{left:28px;top:270px;color:var(--white);font-weight:700;font-size:26px;letter-spacing:-.3px}
  .sub{left:28px;top:299px;color:var(--white);font-weight:700;font-size:16px}
  .about{left:0;top:326px;width:94px;height:19px;background:var(--gold);border-radius:0 10px 10px 0;color:var(--white);font-weight:700;font-size:12px;line-height:19px;padding-left:28px}
  .about-text{left:28px;top:352px;width:316px;color:var(--white);font-size:9.4px;line-height:12px}
  .back .call{left:28px;top:404px;color:var(--white);font-family:"Poppins",sans-serif;font-weight:600;font-size:21px}
  .back .url-bar{top:439px;width:358px}
  .mini-logo{left:368px;top:33px;display:flex;align-items:center;gap:6px}
  .mini-logo .logo-dot{width:24px;height:24px}
  .mini-logo .logo-name{font-size:12px}
  .permit{left:613px;top:35px;width:69px;height:68px;border:1px solid #777;font-family:"Arimo",sans-serif;font-size:8.6px;line-height:11px;text-align:center;padding-top:6px;color:var(--ink)}
  .permit b{font-weight:700}
  .address{left:432px;top:248px;width:188px;height:62px;border:1.5px solid var(--ink);font-family:"Arimo",sans-serif;color:var(--ink);padding:8px 0 0 10px}
  .address .route{font-size:8.4px;text-align:center;margin-right:10px;margin-bottom:9px}
  .address p{font-size:11.5px;line-height:13px}
</style>
</head>
<body>

<section class="card front" aria-label="Mailer front">
  <div class="abs logo-box"><span class="logo-dot"></span><span class="logo-name">812 CLEANING &amp; RESTORATION</span></div>
  <div class="photo" role="img" aria-label="Photo of a child and a puppy lying on a clean white carpet" style="left:26px;top:104px;width:331px;height:182px;background:linear-gradient(135deg,#e9e6e1,#cfc8bd 60%,#f3f1ee)"></div>
  <h1 class="abs title">812 CLEANING &amp;<br>RESTORATION</h1>
  <p class="abs slogan">One Call Cleans It All!</p>
  <div class="abs call-pill">Call Today! 858-555-0147</div>
  <div class="photo frame" role="img" aria-label="Photo of a worker cleaning a tiled roof" style="left:376px;top:182px;width:142px;height:104px;background:linear-gradient(160deg,#c9602f,#a4462a 60%,#7a8f6a)"></div>
  <div class="photo frame" role="img" aria-label="Photo of a window washer on a ladder at a glass facade" style="left:540px;top:182px;width:142px;height:104px;background:linear-gradient(180deg,#b98f5c,#3a3f47 35%,#7f9aa8)"></div>

  <div class="abs band" role="img" aria-label="Raindrop texture background in deep blue"></div>
  <div class="abs services">
    <div class="service"><span class="num">1.</span><div><h3>CARPET CLEANING :</h3><p>Safe Eco-Friendly Truck Mounted Steam Cleaning.</p><p class="tag">Say goodbye to those ugly carpet stains.</p></div></div>
    <div class="service"><span class="num">2.</span><div><h3>WINDOW WASHING:</h3><p>Interior/Exterior, Screens, tracks, frames &amp; sills..</p><p class="tag">Crystal Clear &amp; Streak Free Windows</p></div></div>
    <div class="service"><span class="num">3.</span><div><h3>POWER WASHING:</h3><p>House washing safe for siding, drives, patios &amp; walks.</p><p class="tag">It's like an instant home makeover</p></div></div>
    <div class="service"><span class="num">4.</span><div><h3>WATER DAMAGE:</h3><p>Got Mold or Water damage?</p><p class="tag">Free IR Imaging &amp; Leak Detection</p></div></div>
    <div class="service"><span class="num">5.</span><div><h3>TILE &amp; GROUT:</h3><p>Clean, Restore &amp; Rejuvenate Tile, Grout &amp; Stone.</p><p class="tag">Renew Natural Luster</p></div></div>
    <div class="service"><span class="num">6.</span><div><h3>MAINTENANCE:</h3><p>Professional &amp; dependable repairs.</p><p class="tag">We can Fit It!</p></div></div>
  </div>
  <div class="abs url-bar">www.TidyNorth812.example</div>
</section>

<section class="card back" aria-label="Mailer back">
  <div class="photo" role="img" aria-label="Photo of a technician steam cleaning carpet in an empty room" style="left:0;top:0;width:358px;height:192px;background:linear-gradient(180deg,#d9d7d0,#c8c2b5 70%,#bdb5a5)"></div>
  <div class="photo" role="img" aria-label="Photo of a window cleaner with a squeegee" style="left:0;top:194px;width:118px;height:69px;background:linear-gradient(135deg,#7aa6cf,#2f5f99)"></div>
  <div class="photo" role="img" aria-label="Photo of a repair worker with tool belt in a framed room" style="left:120px;top:194px;width:118px;height:69px;background:linear-gradient(135deg,#d9b98c,#8a6a45)"></div>
  <div class="photo" role="img" aria-label="Photo of tile grout being cleaned" style="left:240px;top:194px;width:118px;height:69px;background:linear-gradient(135deg,#c9c3b3,#8e8a7c)"></div>

  <div class="abs band" role="img" aria-label="Raindrop texture background in deep blue"></div>
  <h2 class="abs eco">ECO FRIENDLY CLEANING</h2>
  <p class="abs sub">San Diego’s Trusted Cleaning Specialists</p>
  <div class="abs about">About us</div>
  <p class="abs about-text">Our company pays special attention to the details of every project to ensure the complete satisfaction of each client. Our goal is to make sure that we leave your home with sparkling kitchen, bathrooms, and floors, organized and tidy living spaces, and refreshing aromas of cleanliness.</p>
  <p class="abs call">Call Today! 858-555-0147</p>
  <div class="abs url-bar">www.TidyNorth812.example</div>

  <div class="abs mini-logo"><span class="logo-dot"></span><span class="logo-name">812 CLEANING &amp; RESTORATION</span></div>
  <div class="abs permit">PRSRT STD<br>ECRWSS<br>U.S. POSTAGE<br><b>PAID</b><br>EDDM RETAIL</div>
  <div class="abs address">
    <div class="route">******************ECRWSS****</div>
    <p>Local<br>Postal Customer</p>
  </div>
</section>

</body>
</html>
```